2367 Halvorsen Avenue Medical Centre

We are looking for a design for Halvorsen Clinic.
We are accepting new patients at this new medical centre grand opening. Walk-ins are welcome.
Our cardiac and vascular surgical specialists are department heads at St Alder's Hospital, a leading teaching hospital in Toronto. These specialists will see cardiovascular consults are well as pre-surgical and post-surgical consultations and follow-ups.
Our lab is affiliated with several nuclear medicine clinics in the GTA.
Our Services Includes:
Family Practice
Cardiology Diagnostics
Cardiac & Vascular Surgical Consultation
Ultrasound & Vascular Testing
Open 6 days a week.
Ample Free Parking
Friendly Staffs

Target Market(s)

New Patients. Families of any age. Ethnic groups including Asians & Africans.

Industry/Entity Type

Medical

Font styles to use
Serif
Sans Serif
Decorative
Script
Other font styles liked:
• Arial calibri, verdana

Requirements
Must have
• Address:
• 2367 Halvorsen Avenue East
• Unit 225
• Scarborough, Ontario
• K7T 2P4
• Tel: (416) 555-0148
Nice to have
• Caring and inviting environment.
• Simple but classy.
• Standout colors.
Should not have
• Busy images. Aside from this, any ideas are welcome.

```html
<!DOCTYPE html>
<html lang="en">
<head>
<meta charset="utf-8">
<title>Halvorsen Clinic</title>
<link rel="stylesheet" href="https://fonts.googleapis.com/css2?family=Open+Sans:ital,wght@0,400;0,600;0,700;1,700&display=swap">
<style>
  :root {
    --blue: #1f8fd6;
    --blue-deep: #1a7fc4;
    --orange: #f08a24;
    --teal: #17a3a8;
    --ink: #1d1d1d;
    --white: #ffffff;
    --photo-light: #f1f4f7;
    --photo-mid: #d9e0e7;
  }
  * { box-sizing: border-box; margin: 0; padding: 0; }
  html, body { width: 872px; height: 1200px; overflow: hidden; background: var(--white); }
  body { font-family: "Open Sans", Arial, sans-serif; color: var(--ink); }
  .poster { position: relative; width: 872px; height: 1200px; overflow: hidden; background: var(--white); }

  .hero-photo {
    position: absolute; left: 0; top: 0; width: 872px; height: 590px;
    background:
      radial-gradient(ellipse 200px 150px at 420px 360px, #e8a99f 0%, rgba(232,169,159,0) 100%),
      radial-gradient(circle 70px at 420px 370px, #d9232c 0%, #d9232c 60%, rgba(217,35,44,0) 100%),
      linear-gradient(160deg, var(--photo-light) 0%, var(--photo-mid) 60%, #eef1f4 100%);
  }
  .hero-wave { position: absolute; left: 0; top: 470px; width: 872px; height: 160px; }

  .title {
    position: absolute; left: 0; top: 164px; width: 872px; text-align: center;
    font-weight: 600; font-size: 69px; letter-spacing: 1px; color: var(--blue);
  }
  .title-rule { position: absolute; left: 43px; top: 247px; width: 770px; height: 2px; background: #3a3a3a; }

  .features { position: absolute; left: 0; top: 630px; list-style: none; }
  .feature {
    position: absolute; left: 0; height: 48px; padding-left: 16px;
    background: var(--orange); color: var(--ink);
    font-size: 29px; line-height: 48px; white-space: nowrap;
    clip-path: polygon(0 0, calc(100% - 18px) 0, 100% 50%, calc(100% - 18px) 100%, 0 100%);
  }
  .feature--walkin { top: 0; width: 459px; }
  .feature--hours { top: 64px; width: 359px; font-weight: 700; font-style: italic; }
  .feature--parking { top: 122px; width: 316px; }
  .feature--staff { top: 181px; width: 247px; }

  .services {
    position: absolute; left: 513px; top: 534px; width: 359px; height: 361px;
    background: var(--blue);
  }
  .services-tab {
    position: absolute; left: 502px; top: 563px; width: 260px; height: 50px;
    background: var(--orange); border-radius: 0 25px 25px 0;
    font-size: 23px; line-height: 50px; padding-left: 14px; color: var(--ink);
  }
  .services-list { position: absolute; left: 544px; top: 642px; list-style: none; width: 320px; }
  .service {
    position: relative; padding-left: 20px; margin-bottom: 18px;
    color: var(--white); font-size: 24px; line-height: 33px;
  }
  .service::before {
    content: "\2605"; position: absolute; left: 0; top: 0; font-size: 14px; color: var(--orange);
  }

  .booking-tab {
    position: absolute; left: 185px; top: 906px; width: 453px; height: 80px;
    background: var(--orange); border-radius: 40px 40px 0 0;
    text-align: center; font-size: 29px; line-height: 62px; color: var(--ink);
  }
  .booking-call {
    position: absolute; left: 78px; top: 962px; width: 660px; height: 95px;
    background: var(--blue-deep); border-radius: 48px; color: var(--white);
    text-align: center; line-height: 95px; font-size: 32px;
  }
  .booking-call strong { font-size: 47px; font-weight: 700; margin-left: 6px; }

  .address-band {
    position: absolute; left: 0; top: 1072px; width: 872px; height: 128px;
    background: var(--teal); color: var(--white); padding: 10px 18px;
  }
  .address-label { font-size: 21px; line-height: 28px; }
  .address-text { font-size: 27px; line-height: 40px; padding-left: 18px; }
</style>
</head>
<body>
<main class="poster">
  <div class="hero-photo" role="img" aria-label="Doctor in a white coat with a stethoscope holding a red heart in cupped hands"></div>
  <svg class="hero-wave" viewBox="0 0 872 160" preserveAspectRatio="none" aria-hidden="true">
    <path d="M0 30 C 120 90 260 120 440 118 C 620 116 760 80 872 60 L872 160 L0 160 Z" fill="#ffffff"/>
    <path d="M0 30 C 120 90 260 120 440 118 C 620 116 760 80 872 60" fill="none" stroke="#17a3a8" stroke-width="8"/>
    <path d="M0 55 C 140 105 280 126 440 126 C 620 124 770 88 872 70" fill="none" stroke="#b9dfe2" stroke-width="3"/>
  </svg>

  <h1 class="title">HALVORSEN CLINIC</h1>
  <div class="title-rule"></div>

  <ul class="features">
    <li class="feature feature--walkin">ACCEPTING WALK-IN PATIENTS</li>
    <li class="feature feature--hours">OPEN 6 DAYS A WEEK</li>
    <li class="feature feature--parking">Ample Free Parking</li>
    <li class="feature feature--staff">Friendly Staffs</li>
  </ul>

  <section class="services"></section>
  <div class="services-tab">SERVICES INCLUDES</div>
  <ul class="services-list">
    <li class="service">Family Practice</li>
    <li class="service">Cardiology Diagnostics</li>
    <li class="service">Cardiac &amp; Vascular Surgical Consultation</li>
    <li class="service">Ultrasound &amp; Vascular</li>
  </ul>

  <div class="booking-tab">TO BOOK APPOINTMENT,</div>
  <div class="booking-call">PLEASE CALL <strong>(416) 555-0148</strong></div>

  <footer class="address-band">
    <p class="address-label">Address:</p>
    <p class="address-text">2367 Halvorsen Avenue East, Unit 225, Scarborough, Ontario<br>K7T 2P4</p>
  </footer>
</main>
</body>
</html>
```